Unique business card design

Boutique coastal hotel suites - in need of clever stand out business card I have uploaded the logo that I had created through quill forge I want something that is clever and stands out from everyone else - 418 Brantwell Avenue tarnhollow Alaska 99571 phone or text 907 -581-6142 www.primemarrowbysuites.com

Target Market(s)

Men and woman

Industry/Entity Type

Boutique coastal hotel

Contact Information for Business Card

Marrowby Suites tarnhollow Alaska marrowby_suites@mailnest.net

Requirements
Must have
• Classy - clever -bold 907-581-6142 call or text

```html
<!DOCTYPE html>
<html lang="en">
<head>
<meta charset="utf-8">
<title>Marrowby Suites – Business Card</title>
<link href="https://fonts.googleapis.com/css2?family=Great+Vibes&display=swap" rel="stylesheet">
<style>
  :root {
    --page: #ffffff;
    --card: #efeae4;
    --ink: #111111;
    --signal-red: #d12427;
    --signal-yellow: #f5d246;
    --signal-navy: #2d526c;
  }
  html, body {
    margin: 0;
    padding: 0;
    width: 1200px;
    height: 927px;
    overflow: hidden;
    background: var(--page);
  }
  .canvas {
    position: relative;
    width: 1200px;
    height: 927px;
  }
  .card {
    position: absolute;
    left: 204px;
    top: 192px;
    width: 822px;
    height: 479px;
    background: var(--card);
    border: 1px solid var(--ink);
    font-family: "Great Vibes", cursive;
    color: var(--ink);
  }
  .stripes {
    position: absolute;
    display: flex;
    gap: 5px;
  }
  .stripes span {
    display: block;
    width: 9px;
    height: 100%;
  }
  .stripes .red { background: var(--signal-red); }
  .stripes .yellow { background: var(--signal-yellow); }
  .stripes .navy { background: var(--signal-navy); }
  .stripes--top-left {
    left: 28px;
    top: 0;
    height: 319px;
  }
  .stripes--bottom-right {
    left: 753px;
    bottom: 0;
    height: 252px;
  }
  .brand-name {
    position: absolute;
    left: 0;
    right: 0;
    top: 80px;
    margin: 0;
    text-align: center;
    font-size: 76px;
    font-weight: 400;
    line-height: 1;
  }
  .divider {
    position: absolute;
    left: 143px;
    width: 531px;
    top: 223px;
    height: 4px;
    background: var(--ink);
  }
  .contact {
    position: absolute;
    left: 0;
    right: 0;
    margin: 0;
    text-align: center;
    font-weight: 400;
    line-height: 1;
    white-space: nowrap;
  }
  .contact--address { top: 280px; font-size: 38px; }
  .contact--phone { top: 337px; font-size: 32px; }
  .contact--web { top: 387px; font-size: 38px; }
</style>
</head>
<body>
  <div class="canvas">
    <section class="card">
      <div class="stripes stripes--top-left" aria-hidden="true">
        <span class="red"></span><span class="yellow"></span><span class="navy"></span>
      </div>

      <h1 class="brand-name">Marrowby Suites</h1>

      <div class="divider" aria-hidden="true"></div>

      <p class="contact contact--address">418 Brantwell Avenue tarnhollow Alaska 99571</p>
      <p class="contact contact--phone">907 -581-6142</p>
      <p class="contact contact--web">www.primemarrowbysuites.com</p>

      <div class="stripes stripes--bottom-right" aria-hidden="true">
        <span class="red"></span><span class="yellow"></span><span class="navy"></span>
      </div>
    </section>
  </div>
</body>
</html>
```